regPersonal Trainer Flyer Design

Reason: I have been very busy with other work and would like to extend the deadline to offer designers the chance to edit and improve designs with my help. Thank you for all the designs that have been sent so far.

```html
<!DOCTYPE html>
<html lang="en">
<head>
<meta charset="utf-8">
<title>Personal Trainer Flyer – Sam Keller</title>
<link rel="stylesheet" href="https://fonts.googleapis.com/css2?family=Bevan&family=Questrial&display=swap">
<style>
  :root {
    --ink: #111111;
    --paper: #ffffff;
    --band-black: #0d0d0d;
    --brand-blue: #4b7cc2;
    --brand-blue-deep: #2f5a9a;
    --label-cyan: #3aa4de;
    --stripe-blue: #3f86dc;
    --photo-dark: #2a2624;
    --photo-warm: #b9a78f;
    --photo-light: #e4dccd;
  }
  * { box-sizing: border-box; margin: 0; padding: 0; }
  html, body { width: 857px; height: 1200px; overflow: hidden; background: var(--paper); }
  .flyer {
    position: relative;
    width: 857px;
    height: 1200px;
    overflow: hidden;
    background: var(--paper);
    font-family: "Bevan", Georgia, serif;
    color: var(--ink);
  }
  .backdrop { position: absolute; left: 0; top: 0; width: 857px; height: 1093px; display: block; }

  .tag {
    position: absolute;
    left: 0;
    padding: 0 12px 0 12px;
    font-size: 22px;
    line-height: 1;
    white-space: nowrap;
    text-transform: uppercase;
    display: flex;
    align-items: center;
    box-shadow: 2px 3px 4px rgba(0,0,0,0.35);
    transform-origin: left center;
  }
  .tag--white { background: var(--paper); }
  .tag--cyan { background: var(--label-cyan); }
  .tag--motivation { top: 12px; height: 76px; width: 375px; transform: rotate(-1.2deg); }
  .tag--goals { top: 108px; height: 70px; width: 466px; transform: rotate(-0.8deg); }
  .tag--help { top: 194px; height: 56px; width: 222px; transform: rotate(-1.5deg); }
  .tag--bored { top: 240px; height: 80px; width: 345px; transform: rotate(-1.6deg); }

  .session-photo {
    position: absolute;
    left: -10px;
    top: 582px;
    width: 412px;
    height: 372px;
    border: 12px solid var(--band-black);
    transform: rotate(-2deg);
    background: linear-gradient(160deg, #ddd7cf 0%, #c9bfb3 40%, #6b5a50 70%, #3c3430 100%);
    box-shadow: 3px 4px 8px rgba(0,0,0,0.4);
  }

  .promise {
    position: absolute;
    right: 0;
    background: var(--paper);
    text-transform: uppercase;
    text-align: right;
    white-space: nowrap;
    font-size: 19px;
    line-height: 1.5;
    padding: 0 10px 0 12px;
    box-shadow: 2px 3px 4px rgba(0,0,0,0.3);
    transform-origin: right center;
  }
  .promise--age { top: 728px; width: 346px; height: 62px; display: flex; align-items: center; justify-content: flex-end; transform: rotate(-1deg); }
  .promise--health { top: 800px; width: 494px; height: 88px; padding-top: 14px; transform: rotate(-1deg); }

  .home-note {
    position: absolute;
    left: 226px;
    top: 944px;
    width: 620px;
    text-align: center;
    white-space: nowrap;
    color: var(--paper);
    font-size: 26px;
    text-transform: uppercase;
  }

  .footer {
    position: absolute;
    left: 0;
    top: 1093px;
    width: 857px;
    height: 107px;
    background: var(--paper);
    font-family: "Questrial", "Century Gothic", sans-serif;
    color: var(--ink);
  }
  .trainer-name {
    position: absolute;
    left: 11px;
    top: 0;
    font-size: 35px;
    letter-spacing: 1px;
    line-height: 50px;
    white-space: nowrap;
  }
  .footer-divider {
    position: absolute;
    left: 333px;
    top: 10px;
    width: 3px;
    height: 88px;
    background: var(--ink);
  }
  .contact {
    position: absolute;
    left: 373px;
    top: 4px;
    font-size: 26px;
    letter-spacing: 0.5px;
    line-height: 48px;
    white-space: nowrap;
  }
  .contact-label { display: inline-block; }
  .contact-label--phone { width: 138px; }
  .contact-label--email { width: 113px; white-space: pre; }
</style>
</head>
<body>
<div class="flyer">
  <svg class="backdrop" viewBox="0 0 857 1093" xmlns="http://www.w3.org/2000/svg">
    <defs>
      <linearGradient id="boxerPhoto" x1="0" y1="0" x2="1" y2="0.3">
        <stop offset="0" stop-color="var(--photo-dark)"/>
        <stop offset="0.45" stop-color="#5a4d44"/>
        <stop offset="0.7" stop-color="var(--photo-warm)"/>
        <stop offset="1" stop-color="var(--photo-light)"/>
      </linearGradient>
      <linearGradient id="blueField" x1="0" y1="0" x2="0" y2="1">
        <stop offset="0" stop-color="var(--brand-blue)"/>
        <stop offset="0.7" stop-color="#4777bb"/>
        <stop offset="1" stop-color="var(--brand-blue-deep)"/>
      </linearGradient>
    </defs>
    <rect role="img" aria-label="Photo of the trainer in a black shirt throwing a punch with red boxing gloves" x="0" y="0" width="857" height="720" fill="url(#boxerPhoto)"/>
    <polygon class="band-black" points="0,330 200,470 402,330 600,470 857,560 857,720 0,720" fill="var(--band-black)"/>
    <polygon role="img" aria-label="Faded blue-tinted photo of gym training" class="field-blue" points="0,466 160,540 402,400 563,555 857,660 857,1093 0,1093" fill="url(#blueField)"/>
    <polyline class="stripe" points="0,438 160,512 402,372 563,527 857,632" fill="none" stroke="var(--stripe-blue)" stroke-width="7"/>
    <polyline class="stripe-edge" points="0,449 160,523 402,383 563,538 857,643" fill="none" stroke="#9cc3f0" stroke-width="1.5"/>
  </svg>

  <div class="tag tag--white tag--motivation">Lacking motivation?</div>
  <div class="tag tag--cyan tag--goals">Not achieving your goals?</div>
  <div class="tag tag--white tag--help">Need help?</div>
  <div class="tag tag--cyan tag--bored">Bored of the gym?</div>

  <div class="session-photo" role="img" aria-label="Photo of the trainer guiding a client through a barbell squat in a gym"></div>

  <div class="promise promise--age">You're never too old</div>
  <div class="promise promise--health">I can help improve your health<br>and well-being</div>

  <p class="home-note">Training can be at your home</p>

  <footer class="footer">
    <div class="trainer-name">Personal Trainer<br>Sam Keller</div>
    <div class="footer-divider"></div>
    <div class="contact">
      <div><span class="contact-label contact-label--phone">Phone :</span>07700900417</div>
      <div><span class="contact-label contact-label--email">Email   :</span>samkeller@fitmail.co.uk</div>
    </div>
  </footer>
</div>
</body>
</html>
```